Packaging Tape Design for Retail / Ecommerce Company

We need a design for custom packing tape for our company. We would like to see two designs for the packaging tape. 1) with the word fragile attached 2) Similiar design without the fragileMinimum resolution is 300 .ppi 3" x 6" or 3" x 12" - If selected, request that font that are used be identified. Orla Hearth Logo and package - Nest Bright! is a tagline we use on documents and correspondence. Looking for a creative design.

Target Market(s)

Mid level to high end consumers

Industry/Entity Type

Retail

Font styles to use
Sans Serif

Requirements
Must have
• logo must be included
• Nest Bright! - must be included
• web address: orlahearth.com
Nice to have
• creativity

```html
<!DOCTYPE html>
<html lang="en">
<head>
<meta charset="utf-8">
<title>Orla Hearth Packing Tape</title>
<link rel="stylesheet" href="https://fonts.googleapis.com/css2?family=Roboto+Condensed:wght@700&display=swap">
<style>
  :root {
    --brick: #7a1a00;
    --linen: #d9d6b2;
    --paper: #ffffff;
    --edge: #8a8a8a;
  }
  html, body {
    margin: 0;
    padding: 0;
    overflow: hidden;
  }
  .sheet {
    position: relative;
    width: 869px;
    height: 1200px;
    background: var(--paper);
    box-sizing: border-box;
    border: 1px solid var(--edge);
    overflow: hidden;
    font-family: "Roboto Condensed", sans-serif;
    font-weight: 700;
  }
  .tape {
    position: absolute;
    top: 108px;
    width: 253px;
    height: 991px;
    display: flex;
  }
  .tape--fragile { left: 125px; }
  .tape--plain { left: 502px; }
  .tape__band--brick {
    width: 153px;
    height: 100%;
    background: var(--brick);
  }
  .tape__band--linen {
    flex: 1;
    height: 100%;
    background: var(--linen);
  }
  .brand {
    position: absolute;
    left: 78px;
    display: flex;
    align-items: center;
    gap: 12px;
    transform: translate(-50%, -50%) rotate(-90deg);
    white-space: nowrap;
    color: var(--linen);
    font-size: 34px;
    letter-spacing: 3px;
    text-transform: uppercase;
  }
  .brand__dot {
    width: 12px;
    height: 12px;
    border-radius: 50%;
    background: var(--linen);
  }
  .tagline {
    position: absolute;
    left: 186px;
    margin: 0;
    transform: translate(-50%, -50%) rotate(-90deg);
    white-space: nowrap;
    text-align: center;
    color: var(--brick);
    font-size: 14px;
    line-height: 20px;
    letter-spacing: 4px;
  }
  .tagline__motto,
  .tagline__web {
    display: block;
  }
  .tagline__motto { text-transform: uppercase; }
  .tagline__web { letter-spacing: 2px; }
  .warning {
    position: absolute;
    left: 213px;
    top: 510px;
    margin: 0;
    transform: translate(-50%, -50%) rotate(-90deg);
    white-space: nowrap;
    color: var(--brick);
    font-size: 62px;
    letter-spacing: 11px;
    line-height: 1;
  }
</style>
</head>
<body>
  <main class="sheet">
    <section class="tape tape--fragile" aria-label="Packing tape with fragile notice">
      <div class="tape__band--brick"></div>
      <div class="tape__band--linen"></div>
      <div class="brand" style="top:172px"><span class="brand__dot"></span>Orla Hearth</div>
      <p class="tagline" style="top:172px"><span class="tagline__motto">Nest Bright!</span><span class="tagline__web">orlahearth.com</span></p>
      <p class="warning">FRAGILE</p>
      <div class="brand" style="top:826px"><span class="brand__dot"></span>Orla Hearth</div>
      <p class="tagline" style="top:826px"><span class="tagline__motto">Nest Bright!</span><span class="tagline__web">orlahearth.com</span></p>
    </section>

    <section class="tape tape--plain" aria-label="Packing tape without notice">
      <div class="tape__band--brick"></div>
      <div class="tape__band--linen"></div>
      <div class="brand" style="top:269px"><span class="brand__dot"></span>Orla Hearth</div>
      <p class="tagline" style="top:269px"><span class="tagline__motto">Nest Bright!</span><span class="tagline__web">orlahearth.com</span></p>
      <div class="brand" style="top:706px"><span class="brand__dot"></span>Orla Hearth</div>
      <p class="tagline" style="top:706px"><span class="tagline__motto">Nest Bright!</span><span class="tagline__web">orlahearth.com</span></p>
    </section>
  </main>
</body>
</html>
```